Contemporary update for a market leader in foodservice distribution

KORVELT is a market leader in foodservice distribution nationwide.
We have recently adopted a new look and feel for our flagship foodservice rewards programme, and we're looking to have our business cards reflect our new aesthetic. Below is a link to our new rewards website to give you a general idea on the look we're after. https://korveltperks.com.au/

Industry/Entity Type

Distribution

Contact Information for Business Card

Must have space for contact name, position, company name and ABN, address, phone number and direct number, fax, email, and web address.

Font styles to use
Serif
Sans Serif

Requirements
Must have
• We'd like a landscape design, with our 'Tip of the Peak' logo incorporated on either the front or the back of the card. The overall design should be contemporary and professional.
Nice to have
• I have included both the full colour and white version of our company logo - our preference is to have the company logo one solid colour (white, or a shade of grey) although we're also open to designs including the full colour logo. If you are able to incorporate a small Facebook and LinkedIn logo, please do so.
Should not have
• Should not have an over-complicated design. No images of globes, or food.

```html
<!DOCTYPE html>
<html lang="en">
<head>
<meta charset="utf-8">
<title>KORVELT Business Card</title>
<link rel="stylesheet" href="https://fonts.googleapis.com/css2?family=Cormorant+Garamond:wght@500&family=Montserrat:wght@800&family=Open+Sans:wght@400;600;700&family=Tinos&display=swap">
<style>
  :root {
    --stage: #2b2b2b;
    --card-black: #050505;
    --brand-green: #04905c;
    --bright-green: #1fae5b;
    --brand-yellow: #f4ea1a;
    --white: #ffffff;
    --soft-white: #e9e9e9;
  }
  * { margin: 0; padding: 0; box-sizing: border-box; }
  html, body { width: 1200px; height: 900px; overflow: hidden; }
  body {
    background: var(--stage);
    font-family: "Open Sans", Arial, sans-serif;
    position: relative;
  }
  .card {
    position: absolute;
    left: 320px;
    width: 560px;
    height: 320px;
    border-radius: 22px;
    overflow: hidden;
    background: var(--card-black);
  }
  .card--front { top: 90px; }
  .card--back { top: 490px; }

  /* Front */
  .front-mark {
    position: absolute;
    left: 0; right: 0; top: 96px;
    display: flex; align-items: center; justify-content: center; gap: 14px;
  }
  .front-mark__dot {
    width: 30px; height: 30px; border-radius: 50%;
    background: var(--bright-green);
  }
  .front-mark__name {
    font-family: "Montserrat", Arial, sans-serif;
    font-weight: 800;
    font-size: 46px;
    color: var(--white);
    letter-spacing: 0.5px;
  }
  .front-web {
    position: absolute; left: 0; right: 0; top: 220px;
    text-align: center;
    font-size: 15px; font-weight: 600;
    color: var(--white);
    letter-spacing: 0.5px;
  }
  .front-web .accent { color: var(--bright-green); }

  /* Back */
  .back-art { position: absolute; inset: 0; }
  .company {
    position: absolute; left: 34px; top: 62px;
    display: flex; align-items: center; gap: 14px;
  }
  .company__dot {
    width: 44px; height: 44px; border-radius: 50%;
    border: 4px solid var(--brand-green);
  }
  .company__name {
    font-family: "Cormorant Garamond", Georgia, serif;
    font-weight: 500;
    font-size: 50px;
    color: var(--white);
    letter-spacing: 2px;
  }
  .contacts {
    position: absolute; left: 34px; top: 172px;
    list-style: none;
  }
  .contacts li {
    display: flex; align-items: center; gap: 10px;
    font-size: 14px; line-height: 20px; color: var(--white);
  }
  .contacts svg { width: 11px; height: 11px; fill: var(--brand-yellow); }
  .person {
    position: absolute; right: 22px; top: 118px;
    text-align: right;
  }
  .person__name {
    font-family: "Tinos", "Times New Roman", serif;
    font-size: 24px; color: var(--brand-yellow);
    line-height: 28px;
    white-space: nowrap;
  }
  .person__role { font-size: 14px; color: var(--white); line-height: 21px; }
  .person__abn { font-size: 14px; color: var(--white); line-height: 21px; }
  .person__abn strong { color: var(--brand-yellow); font-weight: 700; }
  .person__address {
    margin-top: 8px;
    font-size: 13px; line-height: 18px; color: var(--soft-white);
  }
</style>
</head>
<body>
  <section class="card card--front">
    <div class="front-mark">
      <span class="front-mark__dot"></span>
      <span class="front-mark__name">Tip of the Peak</span>
    </div>
    <p class="front-web">www.<span class="accent">korveltperks</span>.com.au</p>
  </section>

  <section class="card card--back">
    <svg class="back-art" viewBox="0 0 560 320" aria-hidden="true">
      <rect width="560" height="320" fill="var(--brand-green)"/>
      <path d="M0,0 L406,0 C374,44 372,152 340,214 C290,282 160,312 0,312 Z" fill="var(--brand-yellow)"/>
      <path d="M0,0 L392,0 C362,42 360,146 330,206 C282,270 158,296 0,296 Z" fill="var(--brand-green)"/>
      <path d="M0,0 L384,0 C354,40 350,140 322,198 C276,262 154,284 0,284 Z" fill="var(--card-black)"/>
    </svg>

    <div class="company">
      <span class="company__dot"></span>
      <span class="company__name">KORVELT</span>
    </div>

    <ul class="contacts">
      <li><svg viewBox="0 0 10 10"><path d="M1 3 Q5 -1 9 3 L8 5 L6 4 L6 3 Q5 2.5 4 3 L4 4 L2 5 Z M2 6 H8 V9 H2 Z"/></svg>555-210-4410</li>
      <li><svg viewBox="0 0 10 10"><path d="M2 1 L4 1 L5 3.5 L3.8 4.5 Q4.8 6.6 6 7.2 L7 6 L9 7 L9 9 Q3 9.5 1 2 Z"/></svg>555-210-4410 (direct)</li>
      <li><svg viewBox="0 0 10 10"><rect x="1" y="1" width="8" height="8" rx="1.5"/></svg>555-730-9182</li>
      <li><svg viewBox="0 0 10 10"><path d="M0.5 2 H9.5 V8.5 H0.5 Z M1.2 2.6 L5 5.6 L8.8 2.6" stroke="var(--card-black)" stroke-width="0.8"/></svg>info@danielharrow.com</li>
      <li><svg viewBox="0 0 10 10"><circle cx="5" cy="5" r="4.3"/><path d="M0.7 5 H9.3 M5 0.7 V9.3" stroke="var(--card-black)" stroke-width="0.8"/></svg>www.korveltperks.com.au</li>
    </ul>

    <div class="person">
      <p class="person__name">Daniel Harrow</p>
      <p class="person__role">President</p>
      <p class="person__abn"><strong>ABN :</strong> 555-210-4410</p>
      <p class="person__address">4820 Alder<br>Boulevard Alder, NC 27512</p>
    </div>
  </section>
</body>
</html>
```